Texting While Driving/Distracted Driving Educational Poster

We are a design-driven nutrition, health, and wellness educational company looking for a fresh, eye-catching educational poster design to promote attentive driving, primarily to young and new drivers. Young, inexperienced drivers (under 20) have the highest proportion of distraction-related fatal crashes, with talking and texting being the most commonly recognized distraction. We hope to draw attention to this issue with an engaging, persuasive poster. The poster will be printed and available for purchase on our website and print catalogs.

Target Market(s)

The audience is American teen to adult drivers and the buyer is educators and healthcare professionals.

Requirements
Must have
• The poster must be 18" x 24" trim size, all fonts in outlines, full color art converted to CMYK.

```html
<!DOCTYPE html>
<html lang="en">
<head>
<meta charset="utf-8">
<title>Sale — Don't Text While You Drive</title>
<link rel="stylesheet" href="https://fonts.googleapis.com/css2?family=Anton&family=Arimo:wght@400&family=Open+Sans:wght@700&display=swap">
<style>
  :root {
    --page: #ffffff;
    --page-edge: #9a9a9a;
    --frame-red: #ff0000;
    --poster-black: #000000;
    --headline-red: #ff0000;
    --asterisk-grey: #b3b3b3;
    --copy-white: #ffffff;
  }
  html, body {
    margin: 0;
    padding: 0;
    overflow: hidden;
    background: var(--page);
  }
  .canvas {
    position: relative;
    width: 1200px;
    height: 900px;
    box-sizing: border-box;
    border: 1px solid var(--page-edge);
    background: var(--page);
    overflow: hidden;
  }
  .poster {
    position: absolute;
    left: 263px;
    top: 0;
    width: 674px;
    height: 900px;
    background: var(--frame-red);
  }
  .poster-field {
    position: absolute;
    left: 19px;
    top: 18px;
    width: 637px;
    height: 862px;
    background: var(--poster-black);
  }
  .headline {
    position: absolute;
    left: 0;
    top: 0;
    width: 637px;
    height: 420px;
  }
  .headline-word {
    font-family: 'Anton', 'Impact', sans-serif;
    fill: var(--headline-red);
  }
  .headline-asterisk {
    fill: var(--asterisk-grey);
  }
  .lead-in {
    position: absolute;
    left: 0;
    width: 100%;
    top: 548px;
    margin: 0;
    text-align: center;
    font-family: 'Open Sans', 'Calibri', sans-serif;
    font-weight: 700;
    font-size: 13px;
    color: var(--copy-white);
  }
  .message {
    position: absolute;
    left: 0;
    width: 100%;
    top: 633px;
    margin: 0;
    text-align: center;
    font-family: 'Arimo', 'Arial', sans-serif;
    font-weight: 400;
    font-size: 37px;
    color: var(--copy-white);
  }
  .disclaimer {
    position: absolute;
    right: 7px;
    bottom: 5px;
    margin: 0;
    font-family: 'Arimo', 'Arial', sans-serif;
    font-size: 12px;
    color: var(--copy-white);
  }
</style>
</head>
<body>
  <div class="canvas">
    <main class="poster">
      <div class="poster-field">
        <svg class="headline" viewBox="0 0 637 420" aria-label="Sale">
          <text class="headline-word" x="56" y="391" font-size="318" textLength="487" lengthAdjust="spacingAndGlyphs">SALE</text>
          <g class="headline-asterisk" transform="translate(580 135)">
            <rect x="-4.5" y="-16" width="9" height="32" rx="1"/>
            <rect x="-4.5" y="-16" width="9" height="32" rx="1" transform="rotate(60)"/>
            <rect x="-4.5" y="-16" width="9" height="32" rx="1" transform="rotate(-60)"/>
          </g>
        </svg>
        <p class="lead-in">OKAY so we got your attention, here’s the msg</p>
        <p class="message">“B smrt. Dnt txt while u DRIVE”</p>
        <p class="disclaimer">* Issued in public interest. Nope, Nothings on Sale.</p>
      </div>
    </main>
  </div>
</body>
</html>
```